Specialised investor in e-mobility and energy wants business card design

We need a business card design that fits our existing corporate design. <The look and feel must be 'sharp'/'clean', dynamic, communicate momentum, professionalism etc (as one would imagine from a firm in the financial sector). We like the idea of a reverse-side of the card that includes the logo, and the name and contact details on the other. We expect the deliverable to be whatever format might be required to be able to get cards printed directly by a service such as marlo cards. Our website is www.obrel.finance

```html
<!DOCTYPE html>
<html lang="en">
<head>
<meta charset="utf-8">
<title>Obrel Finance – Business Card</title>
<link href="https://fonts.googleapis.com/css2?family=Poppins:wght@400;600&family=Questrial&display=swap" rel="stylesheet">
<style>
  :root {
    --bg: #d9dbd8;
    --card-white: #f7f7f5;
    --green-dark: #2c4a22;
    --green-deep: #25401c;
    --green-light: #7db646;
    --white: #ffffff;
  }
  html, body {
    margin: 0;
    width: 1200px;
    height: 900px;
    overflow: hidden;
    background: var(--bg);
  }
  .canvas {
    position: relative;
    width: 1200px;
    height: 900px;
  }
  .card {
    position: absolute;
    width: 560px;
    height: 320px;
    box-shadow: 0 10px 28px rgba(0,0,0,0.22);
    overflow: hidden;
  }
  .card--front {
    left: 110px;
    top: 90px;
    background: linear-gradient(135deg, #ffffff 0%, var(--card-white) 60%, #ececea 100%);
    border-radius: 28px 6px 28px 6px;
    display: flex;
    align-items: center;
    justify-content: center;
  }
  .card--back {
    left: 530px;
    top: 490px;
    background: linear-gradient(120deg, var(--green-dark) 0%, var(--green-deep) 55%, var(--green-dark) 100%);
    border-radius: 6px 44px 6px 44px;
    color: var(--white);
  }
  .wordmark {
    display: flex;
    align-items: center;
    gap: 12px;
    font-family: "Questrial", sans-serif;
    font-weight: 400;
    letter-spacing: 0.5px;
  }
  .wordmark__dot {
    width: 14px;
    height: 14px;
    border-radius: 50%;
    background: var(--green-light);
  }
  .card--front .wordmark { font-size: 50px; color: var(--green-dark); }
  .card--back .wordmark {
    position: absolute;
    right: 34px;
    bottom: 32px;
    font-size: 38px;
    color: var(--white);
  }
  .holder {
    position: absolute;
    left: 34px;
    top: 46px;
    font-family: "Poppins", sans-serif;
  }
  .holder__name {
    margin: 0;
    font-size: 15px;
    font-weight: 600;
    letter-spacing: 0.5px;
    color: var(--green-light);
    text-transform: uppercase;
  }
  .holder__role {
    margin: 2px 0 0;
    font-size: 13px;
    font-weight: 400;
    color: var(--white);
  }
  .contact {
    position: absolute;
    left: 250px;
    top: 40px;
    margin: 0;
    padding: 0;
    list-style: none;
    font-family: "Questrial", sans-serif;
    font-size: 14px;
    line-height: 1;
  }
  .contact__item {
    display: flex;
    align-items: center;
    gap: 10px;
    margin-bottom: 11px;
  }
  .contact__icon {
    width: 14px;
    height: 14px;
    flex: none;
  }
  .divider {
    position: absolute;
    left: 250px;
    right: 0;
    top: 178px;
    height: 1px;
    background: var(--green-light);
    opacity: 0.7;
  }
</style>
</head>
<body>
<main class="canvas">

  <section class="card card--front" aria-label="Card front">
    <div class="wordmark">
      <span class="wordmark__dot"></span>
      <span>Obrel Finance</span>
    </div>
  </section>

  <section class="card card--back" aria-label="Card back">
    <div class="holder">
      <p class="holder__name">Lena Marwick</p>
      <p class="holder__role">Partner</p>
    </div>

    <ul class="contact">
      <li class="contact__item">
        <svg class="contact__icon" viewBox="0 0 14 14" fill="none" stroke="#7db646" stroke-width="1.3">
          <rect x="3.5" y="0.8" width="7" height="12.4" rx="1.3"/>
          <line x1="6" y1="11" x2="8" y2="11"/>
        </svg>
        <span>+41 70 555 0184</span>
      </li>
      <li class="contact__item">
        <svg class="contact__icon" viewBox="0 0 14 14" fill="#7db646">
          <path d="M1 4h12v8H1z"/>
          <path d="M1 4l6 4.5L13 4" fill="none" stroke="#2c4a22" stroke-width="1.2"/>
        </svg>
        <span>lena@obrel.finance</span>
      </li>
      <li class="contact__item">
        <svg class="contact__icon" viewBox="0 0 14 14" fill="none" stroke="#7db646" stroke-width="1.2">
          <circle cx="7" cy="7" r="6"/>
          <ellipse cx="7" cy="7" rx="2.6" ry="6"/>
          <line x1="1" y1="7" x2="13" y2="7"/>
        </svg>
        <span>www.obrel.finance</span>
      </li>
      <li class="contact__item">
        <svg class="contact__icon" viewBox="0 0 14 14" fill="#7db646">
          <path d="M7 0.5a4.5 4.5 0 0 0-4.5 4.5c0 3.4 4.5 8.5 4.5 8.5s4.5-5.1 4.5-8.5A4.5 4.5 0 0 0 7 0.5z"/>
          <circle cx="7" cy="5" r="1.7" fill="#2c4a22"/>
        </svg>
        <span>Obrel Finance S.A. Geneva, Switzerland</span>
      </li>
    </ul>

    <div class="divider"></div>

    <div class="wordmark">
      <span class="wordmark__dot"></span>
      <span>Obrel Finance</span>
    </div>
  </section>

</main>
</body>
</html>
```